Carrow Tessel Hair Extensions needs a packaging design

We need a packaging design for a new hair extension company based in Edmonton, Alberta called Lusine Oro. Our packaging should communicate high quality, luxurious hair that will never tangle or dry out. The product will be marketed to salon professionals as well as clients. We would like to see designs that include but not restricted to the colours gold black and white.

Reason: Although we were very impressed with the designs that came though thus far, we are hoping to receive a few more ideas before making a final decision. Thank you!

Target Market(s)

Women and beauty industry professionals. High end market.

Industry/Entity Type

Hair

Requirements
Must have
• "Highest quality 100% Remi hair!" should be written on the front of the package. In addition, we would like to add text to the back of the packaging as follows:
• Hair Collection and Color Processing:
• Only the highest quality hair is selected which ensures high moisture and nutrient content
• The hair is directly cut from the donor which ensures that the hair cuticle remains intact and always tangle-free
• No chemicals are used in dyeing the hair
• The hair will never fade due to the mild and healthy herbal extract used in the dyeing process which gently penetrates to the inner core of the hair
• Care Instructions:
• Lusine Oro provides only the highest in quality Remi hair that demands very little care to maintain it’s luxurious feel.
• Use a proper extension bristle brush
• Wash the hair with a sulfate-free shampoo and follow with a moisturizing conditioner that is formulated for hair extensions
• Do not apply any type of chemicals to the hair
• We proudly show our immense passion for delivering superior quality in our full product line.
• We insist that it is important for you to know and understand what you are purchasing in your hair extensions. We guarantee the highest quality of our products.
• Lusine Oro is strongly committed to serving their clients with utmost integrity, believing in a foundation of personal and professional ethics and our 20 years service in the beauty industry.
Nice to have
• I would like the background to be white with the "M" in gold. My concern is that this may look too plain, but with that said, I don't want the design to be too busy. Keeping it classy is my main goal.

```html
<!DOCTYPE html>
<html lang="en">
<head>
<meta charset="utf-8">
<title>Lusine Oro – Packaging</title>
<link href="https://fonts.googleapis.com/css2?family=Great+Vibes&family=Arimo:wght@400&display=swap" rel="stylesheet">
<style>
  :root {
    --page: #ffffff;
    --frame: #e2e2e2;
    --panel-dark: #232323;
    --panel-mid: #3a3a3a;
    --gold-deep: #c98a1e;
    --gold-mid: #d9a63a;
    --gold-bright: #fff200;
    --orange: #ff7a00;
    --amber: #ffc400;
    --ribbon: #d3386b;
    --ribbon-text: #ffd400;
    --text-light: #ffffff;
    --tag-string: #9a9a9a;
  }
  html, body {
    margin: 0;
    padding: 0;
    width: 1001px;
    height: 1200px;
    overflow: hidden;
    background: var(--page);
  }
  .canvas { display: block; width: 1001px; height: 1200px; }
  .brand-name { font-family: "Great Vibes", cursive; fill: var(--text-light); }
  .band-name { font-family: "Great Vibes", cursive; fill: #1a1a1a; }
  .tagline { font-family: "Great Vibes", cursive; fill: var(--gold-bright); }
  .claims { font-family: "Arimo", Arial, sans-serif; fill: var(--text-light); letter-spacing: 0.2px; }
  .ribbon-text { font-family: "Arimo", Arial, sans-serif; fill: var(--ribbon-text); font-weight: 400; }
</style>
</head>
<body>
<svg class="canvas" viewBox="0 0 1001 1200" xmlns="http://www.w3.org/2000/svg">
  <defs>
    <linearGradient id="band-grad" x1="0" x2="1" y1="0" y2="0">
      <stop offset="0" stop-color="var(--orange)"/>
      <stop offset="1" stop-color="var(--amber)"/>
    </linearGradient>
    <linearGradient id="band-edge" x1="0" x2="1">
      <stop offset="0" stop-color="#d84a5a"/>
      <stop offset="0.5" stop-color="#ffe600"/>
      <stop offset="1" stop-color="#d84a5a"/>
    </linearGradient>
    <linearGradient id="box-grad" x1="0" x2="0" y1="0" y2="1">
      <stop offset="0.35" stop-color="#ffffff"/>
      <stop offset="1" stop-color="#e3e3e3"/>
    </linearGradient>
    <radialGradient id="dark-grad" cx="0.5" cy="0.35" r="0.7">
      <stop offset="0" stop-color="var(--panel-mid)"/>
      <stop offset="1" stop-color="var(--panel-dark)"/>
    </radialGradient>
    <linearGradient id="gold-grad" x1="0" x2="1" y1="1" y2="0">
      <stop offset="0" stop-color="var(--gold-deep)"/>
      <stop offset="0.55" stop-color="var(--gold-mid)"/>
      <stop offset="0.75" stop-color="var(--gold-bright)"/>
      <stop offset="1" stop-color="var(--gold-deep)"/>
    </linearGradient>
    <linearGradient id="tag-gold" x1="0" x2="1" y1="0" y2="1">
      <stop offset="0" stop-color="var(--gold-deep)"/>
      <stop offset="0.6" stop-color="var(--gold-mid)"/>
      <stop offset="1" stop-color="var(--gold-bright)"/>
    </linearGradient>
  </defs>

  <!-- page frame -->
  <rect x="3" y="3" width="995" height="1194" fill="none" stroke="var(--frame)" stroke-width="3"/>

  <!-- box lid band -->
  <g class="box-lid">
    <rect x="197" y="40" width="338" height="56" fill="url(#band-grad)"/>
    <rect x="197" y="94" width="338" height="7" fill="url(#band-edge)"/>
    <text class="band-name" x="366" y="80" font-size="32" text-anchor="middle">Lusine Oro</text>
  </g>

  <!-- box front -->
  <g class="box-front">
    <rect x="197" y="112" width="340" height="1055" fill="url(#box-grad)"/>
    <path d="M535,330 C528,410 420,432 330,455 C250,478 205,530 197,625 L197,520 C205,480 240,450 320,430 C400,410 520,390 535,320 Z" fill="url(#gold-grad)"/>
    <path d="M200,115 H535 V320 C520,390 400,410 320,430 C240,450 205,480 200,520 Z" fill="url(#dark-grad)" stroke="#ffffff" stroke-width="5" stroke-linejoin="round"/>
    <polygon points="426,115 470,115 535,180 535,138" fill="var(--ribbon)"/>
    <text class="ribbon-text" x="0" y="0" font-size="21" text-anchor="middle" transform="translate(492,141) rotate(45)">NEW</text>

    <circle cx="367" cy="195" r="32" fill="var(--gold-mid)"/>
    <text class="brand-name" x="367" y="295" font-size="52" text-anchor="middle">Lusine Oro</text>
    <text class="tagline" x="367" y="333" font-size="28" text-anchor="middle">Premium Hair Extension</text>
    <text class="claims" x="362" y="357" font-size="12.5" text-anchor="middle">HIGH QUALITY ▪ LUXURIOUS ▪ NO TANGLES</text>
  </g>

  <!-- hang tag -->
  <g class="hang-tag">
    <path d="M662,835 C655,700 640,500 632,400 C625,330 780,320 786,390 C782,500 760,640 745,760 C740,800 740,810 730,822" fill="none" stroke="var(--tag-string)" stroke-width="4" stroke-linecap="round"/>
    <path d="M515,830 Q620,815 730,812 Q800,830 808,900 V1150 Q760,1165 640,1158 Q540,1150 515,1100 Z" fill="url(#tag-gold)"/>
    <path d="M515,828 Q620,818 722,818 Q792,832 796,905 V1138 Q700,1145 605,1122 Q525,1095 515,1040 Z" fill="url(#dark-grad)" stroke="#555" stroke-width="1.5"/>
    <circle cx="675" cy="836" r="5" fill="#ffffff" stroke="#888" stroke-width="1"/>
    <polygon points="515,853 515,878 600,825 560,822" fill="var(--ribbon)"/>
    <text class="ribbon-text" x="0" y="0" font-size="18" text-anchor="middle" transform="translate(547,851) rotate(-35)">NEW</text>

    <circle cx="663" cy="918" r="28" fill="var(--gold-mid)"/>
    <text class="brand-name" x="663" y="1000" font-size="46" text-anchor="middle">Lusine Oro</text>
    <text class="tagline" x="665" y="1031" font-size="24" text-anchor="middle">Premium Hair Extension</text>
    <text class="claims" x="667" y="1048" font-size="11" text-anchor="middle">HIGH QUALITY ▪ LUXURIOUS ▪ NO TANGLES</text>
  </g>
</svg>
</body>
</html>
```